Web Design with a Twist! Not cheap design

Please note that this project is ending at 5pm on Tuesday the 28th of September, Australian Western Standard Time!!

Please also note that this project has now been guaranteed!

This project involves three primary elements:
* Logo design;
* Web design - of additional pages and page elements to fit into a site that is already in design/development;
* Graphic design - various images used on the site.

The following materials are included for the project:
* Project requirements
* Company / Site name
* Company / Site description
* Wireframes for new pages / page elements
* Screenshots of existing designs and accompanying definition of constraints for new designs
* PSDs for existing site designs
* Technical requirements for designs
* Content (to guide designs)

Project Requirements:

* Logo design:
This is a new company / site, so we need a new logo. We want to see what you come up with here without giving too much direction that may restrict creativity. If desired, you may find possible guidance through considering the company name, company description, and the existing site designs. Please note that the current logo in the site is for placeholder purposes only.

* Web design:
We need the following pages (and features) to be designed for the site:
• Home page
• Advertise page
• How it works page
We’ve provided some wireframes for the pages, however we definitely don't want you to be guided by the layout/styling at all - the wireframes are only there to indicate the features that we require on each page only. So please ignore all aspects of the wireframes except for the indications of features and functionality.

* Graphic design:
We need various images to be designed throughout the site. These include:
• The image at the top of the ‘Home’ page – please note we will provide some direction on this asap
• The image at the top of the ‘Advertise’ page – please note we will provide some direction n this asap
• The image at the top of the ‘How it Works’ pages
• The images that accompany each of the left hand menu items on the ‘How it Works’ pages (the main images & thumbnails if that’s part of your design). Please note that these images need to be constructed to match the Headlines for each of the ‘What’, ‘Who’, ‘Where’, etc menu items. These Headlines (and some descriptive text) can be found in the Content section at the end of this brief.
• The map of Australia for the ‘Home’ page
• The images to accompany the pricing section of the ‘Advertise’ page
• The variations of the ‘Days on the finder road’ images that are used on the ‘Home’, ‘Advertise’, and ‘How it Works’ pages. Please note that if you want to use different imagery (or no imagery, dependent upon your design) for the Home and Advertise pages then this is your call.

Company Name:
WorkLoom

Company / Site description:
This site will provide a means for contractors ('advertisers') to easily specify and advertise their services, coupled with a means for employers (‘buyers’) to easily seek out and contact these people.
The site will cater for contractor-side advertisements only; job postings will not be accommodated (turning the traditional job advertisement model on its head).
In general, the functionality of the site is somewhat like a mashup of sites like tallowmesh.com and brindlequay.com. The site will incorporate the following primary features of contractor profile display and search, company profile display, (and an availability calendar for v2 release).

Constraints for designs:
On some of the existing designs you will notice that a number of the elements of the site have already been designed. When constructing your designs, please work in accordance with the following constraints:

You have to keep:
• Colour scheme in the header
• Colour scheme in the top navigation buttons (including text colour and background colour)
• Colour scheme for the buttons like on the Register page

You can ignore:
• The existing placeholder logo
• Border, layout, and colour scheme for page elements (like the lines around and inside the register section on the Register page)
• Design of text fields
• Font colour scheme throughout the site – the orange and grey headlines and body text
• Design and colour scheme of the map of Australia
• The breadcrumbs (whether or not they appear, and their layout, styling, colour scheme etc)
• Dropdown styling (assuming you had to make some; currently not on any pages we’re asking you to do) like on the Browse Profession page
• Profile styling (for the home page featured profiles) like on the Browse Profession page
• Footer styling
• Anything else we haven’t explicitly asked you to keep

Technical requirements for design:
Any site designs in either Layered Photoshop files (PSD's) or Illustrator Drawings (AI). RGB Color. Must fit current site design, we work to 1024 wide screens. Usuable area is defined in site designs that are attached in the Photoshop documents; it's around 960px.
Logo work needs to be Illustrator Drawings (AI) and EPS. Need CMYK images for printing and RGB for screen. Logos must include any special fonts that are used as TTF or Open Type. Logos need Color, Monochrome, Reversed and both Tall and Wide usages.

Content for the 'How it Works' pages - this content should guide the images that appear on each page.
* What
Headline: WorkLoom brings contractors and employers together
Descriptive text: (turns the traditional job search model on its head)
* Who
Headline: WorkLoom is for highly skilled professionals and fast moving companies
Descriptive text:
* Where
Headline: Anywhere in Australia, WorkLoom is working by your side
Descriptive text:
* Why
Headline: There are more than 1 million reasons to love WorkLoom
Descriptive text: In Australia, there are 1 million people who work as contractors in their main job, and a further 100,000 people who are contractors in their second job. That’s a lot of contractors!
* When
Headline: WorkLoom is forming partnerships 24 hours a day
Descriptive text:
* How
Headline: Days on the finder road, with WorkLoom
Descriptive text: Advertise on WorkLoom now, and get your days on the finder road.

Remember
Just remember the wireframes we have submitted are just a guide – we want to see your creativity shine. And above all else - have fun!
Thank you.

Please note the deadline for this design competition 5pm on Tuesday the 28th of September, Australian Western Standard Time.

Just under 3 days away!

The deadline of the project will soon be updated to reflect this.

Hi Designers!

Just to be 100% clear about the deadline - the timer is currently showing 7 hours too many. In other words, the project will end 7 hours before the timer finishes.

I will send a notification if the timer starts to display the correct time. So until then, please remember that the deadline is earlier than it seems!

Thanks

Hi Designers,

A couple of really important points:

Firstly - if everyone could please stick to the theme that we provided in the Photoshop files that would be excellent. It is not possible for us to create a new theme. We're dealing with very tight deadlines, so please just provide designs that fit within the current theme.

Secondly, we were really hoping for more illustrations / graphics to be provided in the designs. We're not a fan of the stock photos of generic business people. So please send through designs that incorporate illustrations / graphics for any imagery.

Also just a reminder that this competition is still ending 7 hours earlier than the timer currently displays.

Thanks.

Target Market(s)

The ‘advertiser’ target market for the site is white collar professionals, in all types of industries. The site will be catering for premium contractors only. The site will be catering for both 'in person' contractors, as well as 'knowledge economy' contractors. The site will not be seeking to compete with quorvane.com, pelbix.com, marnoft.com, or similar sites.

The advertiser target market will also encompass companies and labour hire agencies that have contractors in their workforce.

The ‘buyer’ target market will encompass employers, recruitment agents, and member-to-member hiring.

Requirements
Must have
• As per overview
Nice to have
• As per overview
Should not have
• As per overview

```html
<!DOCTYPE html>
<html lang="en">
<head>
<meta charset="utf-8">
<title>WorkLoom – Advertise</title>
<link rel="stylesheet" href="https://fonts.googleapis.com/css2?family=PT+Sans:wght@400;700&family=Arimo:wght@400;700&display=swap">
<style>
:root{
  --header:#4b5364;
  --panel:#4e5667;
  --orange:#ef5a1c;
  --orange-light:#ff7a2e;
  --orange-logo:#ec6a3c;
  --tab:#9ea3ab;
  --tab-text:#6f7580;
  --page:#f7f7f7;
  --grid:#e2e2e2;
  --white:#ffffff;
  --ink:#4a4a4a;
  --photo-a:#c9cfd8;
  --photo-b:#eef1f4;
  --photo-blue-a:#3c6fa8;
  --photo-blue-b:#9cc0e0;
}
*{box-sizing:border-box;margin:0;padding:0}
html,body{width:1200px;height:1108px;overflow:hidden}
body{
  position:relative;
  background-color:var(--page);
  background-image:
    repeating-linear-gradient(90deg,transparent 0 194px,var(--grid) 194px 195px),
    repeating-linear-gradient(0deg,transparent 0 181px,var(--grid) 181px 182px);
  font-family:"Arimo",Arial,sans-serif;
  color:var(--ink);
}
.abs{position:absolute}

/* header */
.site-header{left:0;top:0;width:1200px;height:100px;background:var(--header)}
.brand{left:108px;top:0;width:117px;height:119px;background:var(--orange-logo);display:flex;align-items:flex-end;justify-content:center;padding-bottom:20px;gap:6px}
.brand-name{font-family:"PT Sans",sans-serif;font-weight:700;font-size:19px;color:var(--white)}
.brand-mark{width:8px;height:8px;background:var(--white);margin-bottom:6px}
.nav-tab{top:71px;height:29px;background:var(--tab);border-radius:5px 5px 0 0;font-family:"PT Sans",sans-serif;font-size:16px;color:var(--tab-text);text-align:center;line-height:31px}
.nav-tab.is-active{background:var(--white);color:var(--header)}
.search{left:911px;top:71px;width:262px;height:26px;background:var(--white);border-radius:3px}
.search svg{position:absolute;left:6px;top:4px}
.search-go{position:absolute;right:2px;top:2px;width:26px;height:22px;background:var(--orange);color:var(--white);font-size:13px;line-height:22px;text-align:center;border-radius:2px}

/* hero */
.hero{left:239px;top:129px;width:716px;height:167px;border-radius:8px;background:linear-gradient(90deg,var(--photo-a),var(--photo-b))}

/* intro panel */
.intro{left:239px;top:311px;width:713px;height:262px;background:var(--panel);border-radius:8px}
.intro-title{left:281px;top:336px;font-family:"PT Sans",sans-serif;font-weight:700;font-size:26px;color:var(--white);display:flex;align-items:center;gap:8px}
.intro-text{left:281px;top:367px;width:340px;font-size:14px;line-height:18.5px;color:var(--white)}
.intro-photo{left:652px;top:315px;width:295px;height:256px;border-radius:8px;background:linear-gradient(135deg,var(--photo-blue-b),var(--photo-blue-a))}

/* register band */
.register-band{left:239px;top:580px;width:713px;height:49px;border-radius:5px;background:linear-gradient(180deg,var(--orange-light),var(--orange))}
.register-btn{left:277px;top:584px;width:172px;height:40px;border-radius:5px;background:linear-gradient(180deg,#5c6270,#2f343d);color:var(--white);font-family:"PT Sans",sans-serif;font-weight:700;font-size:19px;text-align:center;line-height:40px}

/* fees + join */
.lower{left:239px;top:643px;width:713px;height:302px;background:var(--panel);border-radius:8px}
.fees-card{left:249px;top:649px;width:331px;height:288px;background:var(--white);border-radius:10px}
.fees-head{left:253px;top:653px;width:323px;height:36px;border-radius:8px 8px 0 0;background:linear-gradient(180deg,var(--orange-light),var(--orange));font-family:"PT Sans",sans-serif;font-weight:700;font-size:26px;color:var(--white);padding-left:11px;line-height:36px}
.fee-thumb{left:256px;width:88px;height:87px;border:3px solid #9aa0a8;background:linear-gradient(135deg,#d9dde3,#7d8592)}
.fee-price{left:351px;font-family:"PT Sans",sans-serif;font-weight:700;font-size:37px;color:var(--orange);white-space:nowrap}
.fee-price small{font-size:27px}
.fee-note{left:352px;font-family:"PT Sans",sans-serif;font-size:16px;color:var(--orange)}
.fee-divider{left:256px;top:819px;width:306px;height:1px;background:#c8c8c8}
.join-title{left:612px;top:656px;font-family:"PT Sans",sans-serif;font-weight:700;font-size:27px;color:var(--white)}
.join-text{left:616px;top:689px;width:310px;font-size:14px;line-height:18.5px;color:var(--white)}

/* footer */
.footer-band{left:239px;top:955px;width:713px;height:22px;border-radius:5px;background:linear-gradient(180deg,var(--orange-light),var(--orange))}
.footer-col{top:986px;font-family:"PT Sans",sans-serif;font-size:13px;line-height:17.5px;color:#5a5a5a}
.footer-col h4{font-size:13px;color:var(--orange);font-weight:700}
.copyright{left:787px;top:986px;font-family:"PT Sans",sans-serif;font-size:13px;color:#5a5a5a}
</style>
</head>
<body>

<header class="abs site-header"></header>
<div class="abs brand"><span class="brand-name">WorkLoom</span><span class="brand-mark"></span></div>

<nav>
  <div class="abs nav-tab" style="left:249px;width:96px">Home</div>
  <div class="abs nav-tab" style="left:352px;width:96px">Find</div>
  <div class="abs nav-tab is-active" style="left:457px;width:108px">Advertise</div>
  <div class="abs nav-tab" style="left:575px;width:128px">How it Works</div>
  <div class="abs nav-tab" style="left:711px;width:81px">Blog</div>
  <div class="abs nav-tab" style="left:800px;width:84px">Login</div>
</nav>

<div class="abs search">
  <svg width="20" height="20" viewBox="0 0 20 20"><circle cx="8" cy="8" r="6" fill="none" stroke="#8a8f98" stroke-width="2.5"/><line x1="12.5" y1="12.5" x2="18" y2="18" stroke="#8a8f98" stroke-width="3" stroke-linecap="round"/></svg>
  <span class="search-go">Go</span>
</div>

<div class="abs hero" role="img" aria-label="Two smiling young professionals in a bright office"></div>

<section>
  <div class="abs intro"></div>
  <h2 class="abs intro-title">
    <svg width="20" height="20" viewBox="0 0 20 20"><g stroke="#fff" stroke-width="3.2" stroke-linecap="round"><line x1="10" y1="2" x2="10" y2="18"/><line x1="3" y1="6" x2="17" y2="14"/><line x1="3" y1="14" x2="17" y2="6"/></g></svg>
    Days on the Finder Road
  </h2>
  <p class="abs intro-text">Lorem Ipsum is simply dummy text of the printing and typesetting industry. Lorem Ipsum has been the industry's standard dummy text ever since the 1500s, when an unknown printer took a galley of type and scrambled it to make a type specimen book. It has survived not only five centuries, but also the leap into electronic typesetting, remaining essentially unchanged. It was popularised in the 1960s with the release of Lettrafix sheets containing Lorem Ipsum passages.</p>
  <div class="abs intro-photo" role="img" aria-label="Business team meeting around a table with laptops"></div>
</section>

<div class="abs register-band"></div>
<div class="abs register-btn">Register Now</div>

<section>
  <div class="abs lower"></div>
  <div class="abs fees-card"></div>
  <h3 class="abs fees-head">Our Fees</h3>

  <div class="abs fee-thumb" style="top:717px" role="img" aria-label="Business people shaking hands"></div>
  <div class="abs fee-price" style="top:712px">$149.95 <small>year</small></div>
  <div class="abs fee-note" style="top:759px">Includes one team member</div>

  <div class="abs fee-divider"></div>

  <div class="abs fee-thumb" style="top:833px" role="img" aria-label="Portrait of a businessman in a suit"></div>
  <div class="abs fee-price" style="top:826px">$29.95<small>year</small></div>
  <div class="abs fee-note" style="top:871px">per extra team member</div>

  <h2 class="abs join-title">Join Us Now!</h2>
  <p class="abs join-text">Lorem Ipsum is simply dummy text of the printing and typesetting industry. Lorem Ipsum has been the industry's standard dummy text ever since the 1500s, when an unknown printer took a galley of type and scrambled it to make a type specimen book. It has survived not only five centuries, but also the leap into electronic typesetting, remaining essentially unchanged. It was popularised in the 1960s with the release of Lettrafix sheets containing Lorem Ipsum passages, and more recently with desktop publishing software like Quillset Composer including versions of Lorem Ipsum.</p>
</section>

<footer>
  <div class="abs footer-band"></div>
  <div class="abs footer-col" style="left:237px"><h4>The Service</h4>About<br>Browse<br>Log In</div>
  <div class="abs footer-col" style="left:420px"><h4>Support</h4>Contact Us<br>FAQ</div>
  <div class="abs footer-col" style="left:601px"><h4>Legal</h4>Privacy Policy<br>Temrs &amp; Conditions</div>
  <div class="abs copyright">© 2010 Loomfield Pty Ltd</div>
</footer>

</body>
</html>
```